Steady Harbor Claims Group Business card

Need a business card that stands out that includes name of company,(above) Owners name Moira Lindqvist phone#517-362-4408 email# SteadyHarborCG@mailvane.com and website www.Steadyharborclaimsgroup.net. This is a medical billing company so the card has to relate to that or relate to increasing revenue

```html
<!DOCTYPE html>
<html lang="en">
<head>
<meta charset="utf-8">
<title>Steady Harbor Claims Group – Business Card</title>
<link rel="stylesheet" href="https://fonts.googleapis.com/css2?family=Cinzel:wght@600&family=Roboto:wght@400;500&display=swap">
<style>
  :root {
    --backdrop: #e9e7e4;
    --card-black: #1b1c1e;
    --card-black-deep: #111213;
    --emboss: #2a2b2e;
    --brand-blue: #1a7fd0;
    --brand-green: #86c832;
    --text-light: #f2f2f2;
    --text-muted: #d6d6d6;
  }
  * { margin: 0; padding: 0; box-sizing: border-box; }
  html, body { width: 1200px; height: 716px; overflow: hidden; }
  body {
    background: var(--backdrop);
    font-family: "Roboto", Arial, sans-serif;
    position: relative;
  }
  .card {
    position: absolute;
    top: 204px;
    width: 540px;
    height: 309px;
    border-radius: 4px;
    overflow: hidden;
    box-shadow: 0 10px 24px rgba(0,0,0,0.22);
  }
  .card--back {
    left: 40px;
    background: var(--card-black-deep);
    display: flex;
    align-items: center;
    justify-content: center;
  }
  .card--back .brand-name {
    color: var(--emboss);
    font-size: 30px;
    text-align: center;
    line-height: 1.25;
  }
  .brand-name {
    font-family: "Cinzel", Georgia, serif;
    font-weight: 600;
    letter-spacing: 0.5px;
  }
  .card--front { left: 620px; background: var(--card-black); }
  .card__waves { position: absolute; inset: 0; }
  .card__brand {
    position: absolute;
    top: 34px;
    right: 34px;
    display: flex;
    align-items: center;
    gap: 12px;
  }
  .card__brand .mark {
    width: 18px; height: 18px; border-radius: 50%;
    background: var(--brand-green);
  }
  .card__brand .brand-name {
    color: var(--brand-blue);
    font-size: 22px;
    line-height: 1.15;
    text-align: center;
  }
  .contact-list {
    position: absolute;
    top: 96px;
    left: 30px;
    list-style: none;
    color: var(--text-light);
    font-size: 13px;
  }
  .contact-list li {
    display: flex;
    align-items: center;
    gap: 9px;
    margin-bottom: 5px;
  }
  .contact-list svg { width: 11px; height: 11px; flex: none; }
  .owner {
    position: absolute;
    right: 40px;
    bottom: 34px;
    text-align: left;
    color: var(--text-light);
  }
  .owner__name { font-size: 20px; font-weight: 500; }
  .owner__role { font-size: 12px; color: var(--text-muted); margin-top: 4px; padding-left: 70px; }
</style>
</head>
<body>

  <section class="card card--back" aria-label="Card back">
    <p class="brand-name">Steady Harbor<br>Claims Group</p>
  </section>

  <section class="card card--front" aria-label="Card front">
    <svg class="card__waves" viewBox="0 0 540 309" preserveAspectRatio="none" aria-hidden="true">
      <path d="M0,175 C140,185 250,260 540,232 L540,309 L0,309 Z" fill="var(--brand-blue)"/>
      <path d="M0,150 C150,170 280,250 540,222 L540,228 C280,258 150,185 0,165 Z" fill="var(--brand-green)"/>
      <path d="M0,160 C120,178 230,232 420,232 C300,228 140,190 0,172 Z" fill="var(--brand-green)" opacity="0.85"/>
    </svg>

    <div class="card__brand">
      <span class="mark"></span>
      <p class="brand-name">Steady Harbor<br>Claims Group</p>
    </div>

    <ul class="contact-list">
      <li>
        <svg viewBox="0 0 12 12"><path d="M2.5 1h2l1 3-1.3 1a6 6 0 0 0 2.8 2.8L8 6.5l3 1v2c0 .8-.7 1.5-1.5 1.5A8.5 8.5 0 0 1 1 2.5C1 1.7 1.7 1 2.5 1Z" fill="var(--brand-green)"/></svg>
        517-362-4408
      </li>
      <li>
        <svg viewBox="0 0 12 12"><rect x="1" y="2.5" width="10" height="7" rx="1" fill="var(--brand-green)"/><path d="M1.5 3l4.5 3.5L10.5 3" stroke="var(--card-black)" stroke-width="1" fill="none"/></svg>
        SteadyHarborCG@mailvane.com
      </li>
      <li>
        <svg viewBox="0 0 12 12"><circle cx="6" cy="6" r="5" fill="var(--brand-green)"/><circle cx="6" cy="6" r="2" fill="var(--card-black)"/></svg>
        www.Steadyharborclaimsgroup.net
      </li>
    </ul>

    <div class="owner">
      <p class="owner__name">Moira Lindqvist</p>
      <p class="owner__role">Owner</p>
    </div>
  </section>

</body>
</html>
```